Update Old OR create new Website

Current Website is looking a bit old, I did this one a few years back.

Would like a fresh new look, current website wordpress theme is " the Kora theme" from plantowne and I just purchased this theme - "boltaro" also from plantowne, I quite like the look of - http://boltaro.nuvamark-skins.com/tech-business/ and if we could get somthing simlar would be great.

current website is at http://www.quelp.com.au, have been playing around with the slider that i like.

I have said 5 pages to be designed but really it is just a 5 page website where most pages will look the same.

Any questions please let me know

Target Market(s)

Business

Coding

Coded - Design and coding required

Number of Pages Required

5+ page

Font styles to use
Sans Serif

Colors
33a6d7
0292cd
ffffff
0255a3

Requirements
Must have
• Device compatibility - pc, tablet, phone
Nice to have
• video
Should not have
• vunerabilities. Must also use images that will expire or disappear, ie must be uploaded to site not links to elsewhere.

```html
<!DOCTYPE html>
<html lang="en">
<head>
<meta charset="utf-8">
<title>Quelp Technologies</title>
<link rel="stylesheet" href="https://fonts.googleapis.com/css2?family=Montserrat:wght@400;600;700&family=Open+Sans:wght@400;600;700&display=swap">
<style>
:root{
  --sky:#33a6d7;
  --blue:#0292cd;
  --navy:#0255a3;
  --white:#ffffff;
  --ink:#2b2f36;
  --muted:#7a808a;
  --line:#e3e7ec;
  --pale:#e6f5fc;
  --grey:#f4f5f7;
  --dark:#2a2c30;
  --darker:#1d1f22;
}
*{box-sizing:border-box;margin:0;padding:0}
html,body{width:1200px;height:4636px;overflow:hidden}
body{font-family:"Open Sans",Arial,sans-serif;color:var(--ink);background:var(--white);position:relative}
h1,h2,h3,h4{font-family:"Montserrat",Arial,sans-serif}
section,header{position:absolute;left:0;width:1200px}
.btn{display:inline-block;font-family:"Montserrat",Arial,sans-serif;font-size:13px;font-weight:600;letter-spacing:.5px;padding:12px 20px;text-transform:uppercase}
.btn-solid{background:var(--blue);color:var(--white)}
.btn-ghost{border:2px solid var(--white);color:var(--white);padding:10px 18px}
.btn-line{border:2px solid var(--blue);color:var(--navy);background:var(--white);padding:8px 14px;font-size:11px}
.section-title{text-align:center;font-size:26px;font-weight:700;color:var(--navy);letter-spacing:1px}
.section-title::after{content:"";display:block;width:50px;height:3px;background:var(--sky);margin:12px auto 0}
.section-sub{text-align:center;font-size:14px;color:var(--muted);margin-top:14px}

/* top bar */
.topbar{top:0;height:36px;background:var(--darker);color:#cfd3d8;font-size:12px;display:flex;align-items:center;justify-content:space-between;padding:0 40px}
.topbar .social{display:flex;align-items:center;gap:8px}
.topbar .social i{display:inline-block;width:10px;height:10px;border-radius:50%;background:var(--sky)}
.topbar .call{font-weight:600;color:var(--white)}

/* header */
.site-header{top:36px;height:116px;background:var(--white);display:flex;align-items:center;justify-content:space-between;padding:0 40px;box-shadow:0 2px 6px rgba(0,0,0,.08)}
.brand{display:flex;align-items:center;gap:12px;font-family:"Montserrat",Arial,sans-serif;font-weight:700;font-size:24px;color:var(--navy)}
.brand .mark{width:34px;height:34px;background:var(--sky)}
.main-nav{display:flex;gap:34px;font-family:"Montserrat",Arial,sans-serif;font-size:14px;font-weight:600;color:var(--ink)}

/* hero */
.hero{top:152px;height:456px;background:radial-gradient(ellipse at 55% 55%,#1f6fc2 0%,#0b3a78 45%,#051a3a 100%);color:var(--white);text-align:center}
.hero h1{font-size:54px;letter-spacing:3px;margin-top:110px;font-weight:700}
.hero p{font-size:16px;max-width:720px;margin:30px auto 0;line-height:1.6}
.hero .actions{margin-top:48px;display:flex;justify-content:center;gap:14px}
.hero .arrow{position:absolute;top:200px}
.hero .arrow.left{left:34px}
.hero .arrow.right{right:34px}

/* services */
.services{top:608px;height:692px;background:var(--white)}
.services .section-title{margin-top:76px}
.service-cards{display:flex;justify-content:center;gap:30px;margin-top:100px}
.service-card{width:240px;height:340px;background:var(--white);box-shadow:0 4px 14px rgba(0,0,0,.12);text-align:center;padding-top:26px}
.service-card .icon{width:100px;height:100px;border-radius:50%;background:var(--blue);margin:0 auto;display:flex;align-items:center;justify-content:center}
.service-card .icon.alt{background:var(--navy)}
.service-card h3{font-size:16px;color:var(--navy);margin-top:24px}
.service-card p{font-size:12px;color:var(--muted);line-height:1.6;padding:12px 24px 0}
.service-card .btn{margin-top:20px;font-size:10px;padding:8px 14px}

/* help */
.help{top:1300px;height:428px;background:var(--pale)}
.help .person{position:absolute;left:70px;top:40px;width:360px;height:388px;background:linear-gradient(180deg,#dbe9f2,#2d3440 70%)}
.help .copy{position:absolute;left:480px;top:78px;width:640px}
.help h2{font-size:28px;line-height:1.3;color:var(--navy);font-weight:700}
.help p{font-size:14px;color:var(--muted);line-height:1.7;margin-top:22px}
.help .btn{margin-top:30px}

/* testimonials */
.testimonials{top:1728px;height:452px;background:linear-gradient(180deg,#2c3038,#3d4350 60%,#23262c)}
.testimonials .section-title{color:var(--white);margin-top:64px}
.quotes{display:flex;justify-content:center;gap:20px;margin-top:78px}
.quote{width:330px;height:196px;background:rgba(255,255,255,.18);padding:20px 22px;color:var(--white);position:relative}
.quote h4{font-size:15px;font-weight:600}
.quote p{font-size:12px;line-height:1.6;margin-top:10px;color:#e3e6ea}
.quote .who{position:absolute;left:22px;bottom:18px;display:flex;align-items:center;gap:10px;font-size:13px;font-weight:600}
.quote .who span.role{display:block;font-weight:400;font-size:11px;color:#c9ced4}
.quote .avatar{width:34px;height:34px;border-radius:50%;background:#8d96a3}

/* devices */
.devices{top:2180px;height:560px;background:var(--white)}
.devices .mockup{position:absolute;left:120px;top:120px;width:400px;height:330px;background:linear-gradient(135deg,#e9eef3,#b8c2cc);border-radius:6px}
.features{position:absolute;left:620px;top:100px;width:470px}
.feature{display:flex;gap:16px;margin-bottom:40px}
.feature svg{flex:none}
.feature h4{font-size:17px;color:var(--ink);font-weight:600}
.feature p{font-size:13px;color:var(--muted);line-height:1.6;margin-top:6px}

/* solutions */
.solutions{top:2740px;height:620px;background:var(--grey)}
.solutions .section-title{margin-top:70px}
.solution-list{display:flex;justify-content:center;gap:40px;margin-top:56px;position:relative}
.solution{width:230px;text-align:center}
.solution .ring{width:128px;height:128px;border-radius:50%;border:3px solid var(--sky);margin:0 auto;display:flex;align-items:center;justify-content:center;background:var(--white)}
.solution .ring.active{background:var(--pale)}
.solution h4{font-size:14px;color:var(--navy);margin-top:34px;font-weight:700}
.solution h4.active{color:var(--sky)}
.solution p{font-size:12px;color:var(--muted);line-height:1.6;margin-top:12px}
.solution .btn{margin-top:22px}
.solution-link{position:absolute;top:64px;left:260px;width:680px;height:2px;background:var(--sky)}

/* cta */
.cta{top:3360px;height:448px;background:var(--navy);color:var(--white);text-align:center}
.cta h2{font-size:26px;line-height:1.45;margin-top:76px;font-weight:700}
.cta p{font-size:14px;line-height:1.7;max-width:960px;margin:32px auto 0;color:#dbe7f3}
.cta .actions{margin-top:44px;display:flex;justify-content:center;gap:14px}

/* partners */
.partners{top:3808px;height:260px;background:var(--white);display:flex;justify-content:center;align-items:center;gap:40px}
.partner{width:140px;height:80px;border:1px solid var(--line);background:var(--grey)}

/* contact */
.contact{top:4068px;height:512px;background:var(--dark);color:var(--white)}
.contact .section-title{color:var(--white);margin-top:72px}
.contact-lines{display:flex;justify-content:center;gap:60px;margin-top:56px;font-size:16px}
.contact-lines span{display:flex;align-items:center;gap:12px}
.contact-form{position:absolute;left:100px;top:272px;width:1000px}
.contact-form .row{display:flex;gap:16px}
.field{flex:1;height:44px;background:var(--white);color:#8a9099;font-size:13px;padding:13px 14px}
.field.message{height:100px;margin-top:18px}
.contact-form .send{display:block;width:180px;margin:24px auto 0;text-align:center}

.footer{top:4580px;height:56px;background:var(--darker);color:#b8bdc4;font-size:13px;text-align:center;line-height:56px}
</style>
</head>
<body>

<div class="topbar" style="position:absolute;left:0;width:1200px">
  <div class="social">Follow us: <i></i><i></i><i></i><i></i></div>
  <div class="call">CALL NOW! 1300 555 018</div>
</div>

<header class="site-header">
  <div class="brand"><span class="mark"></span>Quelp Technologies</div>
  <nav class="main-nav">
    <span>HOME</span><span>SERVERS</span><span>NETWORKS</span><span>MANAGED IT</span><span>WEB</span><span>APPS</span><span>INTERNET</span><span>CONTACT</span>
  </nav>
</header>

<section class="hero" role="img" aria-label="Hero background: glowing blue digital network">
  <h1>QUELP TECHNOLOGY</h1>
  <p>Quelp Technologies provides the design, support and maintenance for quality I.T Systems for clients to drive, change and grow.</p>
  <div class="actions"><span class="btn btn-solid">Read More</span><span class="btn btn-ghost">Contact Us</span></div>
  <svg class="arrow left" width="20" height="40" viewBox="0 0 20 40"><path d="M18 2 2 20l16 18" fill="none" stroke="#fff" stroke-width="3"/></svg>
  <svg class="arrow right" width="20" height="40" viewBox="0 0 20 40"><path d="M2 2l16 18L2 38" fill="none" stroke="#fff" stroke-width="3"/></svg>
</section>

<section class="services">
  <h2 class="section-title">OUR SERVICES</h2>
  <p class="section-sub">Quelp Technologies staff are not just short-term problem solvers – they are advanced systems</p>
  <div class="service-cards">
    <div class="service-card">
      <div class="icon"><svg width="50" height="44" viewBox="0 0 50 44"><rect x="2" y="2" width="46" height="30" rx="2" fill="none" stroke="#fff" stroke-width="3"/><path d="M18 42h14M25 32v10" stroke="#fff" stroke-width="3"/></svg></div>
      <h3>MANAGED IT</h3>
      <p>Our team keeps your systems running smoothly so you can focus on running your business.</p>
      <span class="btn btn-solid">Read More</span>
    </div>
    <div class="service-card">
      <div class="icon alt"><svg width="54" height="36" viewBox="0 0 54 36"><path d="M14 34a12 12 0 0 1 0-24 16 16 0 0 1 30 4 10 10 0 0 1 0 20z" fill="none" stroke="#fff" stroke-width="3"/></svg></div>
      <h3>PRIVATE CLOUD</h3>
      <p>Secure hosted storage and services that grow with your team, wherever they happen to work.</p>
      <span class="btn btn-solid">Read More</span>
    </div>
    <div class="service-card">
      <div class="icon"><svg width="44" height="46" viewBox="0 0 44 46"><g fill="none" stroke="#fff" stroke-width="3"><rect x="2" y="2" width="40" height="12"/><rect x="2" y="17" width="40" height="12"/><rect x="2" y="32" width="40" height="12"/></g><g fill="#fff"><circle cx="34" cy="8" r="2"/><circle cx="34" cy="23" r="2"/><circle cx="34" cy="38" r="2"/></g></svg></div>
      <h3>SERVERS</h3>
      <p>Reliable server design, setup and upkeep tailored to the way your office actually works.</p>
      <span class="btn btn-solid">Read More</span>
    </div>
    <div class="service-card">
      <div class="icon alt"><svg width="48" height="48" viewBox="0 0 48 48"><g fill="none" stroke="#fff" stroke-width="3"><circle cx="24" cy="24" r="21"/><ellipse cx="24" cy="24" rx="9" ry="21"/><path d="M3 24h42M7 13h34M7 35h34"/></g></svg></div>
      <h3>WEB</h3>
      <p>Modern websites built to load fast, look sharp and work on every screen size.</p>
      <span class="btn btn-solid">Read More</span>
    </div>
  </div>
</section>

<section class="help">
  <div class="person" role="img" aria-label="Photo of a smiling support consultant gesturing toward the text"></div>
  <div class="copy">
    <h2>NEED ANY HELP? OUR QUELP TECHNOLOGIES SUPPORT WILL HELP YOU.</h2>
    <p>Our friendly support desk is ready to answer your questions, fix problems fast and plan upgrades with you. Call us or send a message and a local technician will get back to you the same business day with clear advice.</p>
    <span class="btn btn-solid">Contact Us</span>
  </div>
</section>

<section class="testimonials" role="img" aria-label="Background photo of a dim office, overlaid with client testimonials">
  <h2 class="section-title">OUR TESTIMONIALS</h2>
  <div class="quotes">
    <div class="quote">
      <h4>"Remarkable Style"</h4>
      <p>The new network was installed quickly and has run without a single issue since day one.</p>
      <div class="who"><span class="avatar"></span><div>Dale Morris<span class="role">Customer</span></div></div>
    </div>
    <div class="quote">
      <h4>"Easy &amp; Fun"</h4>
      <p>Friendly people who explain things clearly and always answer the phone when we need them.</p>
      <div class="who"><span class="avatar"></span><div>Nina Lowe<span class="role">Customer</span></div></div>
    </div>
    <div class="quote">
      <h4>"Satisfied Clients"</h4>
      <p>Our whole office moved to the cloud over a weekend and nobody lost any work.</p>
      <div class="who"><span class="avatar"></span><div>Owen Price<span class="role">Customer</span></div></div>
    </div>
  </div>
</section>

<section class="devices">
  <div class="mockup" role="img" aria-label="Desktop monitor and smartphone showing the Quelp Technologies site"></div>
  <div class="features">
    <div class="feature">
      <svg width="34" height="34" viewBox="0 0 34 34"><rect x="2" y="4" width="30" height="20" fill="none" stroke="#0255a3" stroke-width="2"/><path d="M12 32h10M17 24v8" stroke="#0255a3" stroke-width="2"/></svg>
      <div><h4>Discovery &amp; Strategy</h4><p>Quelp Technologies staff are not just short-term problem solvers – they are advanced systems.</p></div>
    </div>
    <div class="feature">
      <svg width="34" height="34" viewBox="0 0 34 34"><path d="M4 30 26 8l4 4L8 34H4zM22 4l8 8" fill="none" stroke="#0255a3" stroke-width="2"/></svg>
      <div><h4>User Experience Design</h4><p>Quelp Technologies staff are not just short-term problem solvers – they are advanced systems.</p></div>
    </div>
    <div class="feature">
      <svg width="34" height="34" viewBox="0 0 34 34"><rect x="9" y="2" width="16" height="30" rx="2" fill="none" stroke="#0255a3" stroke-width="2"/><circle cx="17" cy="27" r="1.6" fill="#0255a3"/></svg>
      <div><h4>Mobile App Development</h4><p>Quelp Technologies staff are not just short-term problem solvers – they are advanced systems.</p></div>
    </div>
  </div>
</section>

<section class="solutions">
  <h2 class="section-title">OUR SOLUTIONS</h2>
  <p class="section-sub">Practical digital services that help local businesses reach more customers and work smarter.</p>
  <div class="solution-list">
    <div class="solution-link"></div>
    <div class="solution">
      <div class="ring"><svg width="56" height="48" viewBox="0 0 56 48"><rect x="2" y="2" width="52" height="34" fill="none" stroke="#0292cd" stroke-width="3"/><path d="M20 46h16M28 36v10" stroke="#0292cd" stroke-width="3"/></svg></div>
      <h4>WEBSITE DESIGN</h4>
      <p>Clean, responsive sites that reflect your brand and turn visitors into enquiries.</p>
      <span class="btn btn-line">Read More</span>
    </div>
    <div class="solution">
      <div class="ring active"><svg width="56" height="48" viewBox="0 0 56 48"><rect x="2" y="6" width="52" height="32" fill="none" stroke="#33a6d7" stroke-width="3"/><path d="M10 30l12-12 8 8 14-14" fill="none" stroke="#33a6d7" stroke-width="3"/></svg></div>
      <h4 class="active">DIGITAL STRATEGY</h4>
      <p>A clear plan for the tools, channels and budget that suit your goals.</p>
      <span class="btn btn-line">Read More</span>
    </div>
    <div class="solution">
      <div class="ring"><svg width="52" height="52" viewBox="0 0 52 52"><g fill="none" stroke="#0292cd" stroke-width="3"><circle cx="26" cy="26" r="12"/><path d="M26 2v10M26 40v10M2 26h10M40 26h10"/></g></svg></div>
      <h4>WEB MARKETING</h4>
      <p>Search, email and social campaigns measured against real business results.</p>
      <span class="btn btn-line">Read More</span>
    </div>
    <div class="solution">
      <div class="ring"><svg width="56" height="40" viewBox="0 0 56 40"><path d="M14 38a12 12 0 0 1 0-24 16 16 0 0 1 30 4 10 10 0 0 1 0 20z" fill="none" stroke="#0292cd" stroke-width="3"/></svg></div>
      <h4>REMARKETING</h4>
      <p>Reconnect with past visitors and bring them back when they are ready to buy.</p>
      <span class="btn btn-line">Read More</span>
    </div>
  </div>
</section>

<section class="cta">
  <h2>WHAT WOULD IT TAKE FOR YOUR INFORMATION SYSTEMS TO ACTUALLY IMPROVE<br>THE PERFORMANCE OF YOUR ORGANISATION?</h2>
  <p>Through Quelp Technologies, companies outsource all the expertise they need to secure their systems and optimise the output of their people and IT resources – without the expense of maintaining large internal IT departments.</p>
  <div class="actions"><span class="btn btn-solid">Read More</span><span class="btn btn-ghost">Contact Us</span></div>
</section>

<section class="partners">
  <div class="partner"></div><div class="partner"></div><div class="partner"></div><div class="partner"></div><div class="partner"></div><div class="partner"></div>
</section>

<section class="contact">
  <h2 class="section-title">CONTACT US</h2>
  <div class="contact-lines">
    <span><svg width="22" height="22" viewBox="0 0 22 22"><path d="M5 2l4 4-2 3a12 12 0 0 0 6 6l3-2 4 4-3 3C9 20 2 13 2 5z" fill="#fff"/></svg>1300 555 018</span>
    <span><svg width="24" height="18" viewBox="0 0 24 18"><rect x="1" y="1" width="22" height="16" fill="none" stroke="#fff" stroke-width="2"/><path d="M1 1l11 9 11-9" fill="none" stroke="#fff" stroke-width="2"/></svg>info@quelptech.com.au</span>
  </div>
  <div class="contact-form">
    <div class="row"><div class="field">Your Name (required)</div><div class="field">Your Email (required)</div><div class="field">Subject</div></div>
    <div class="field message">Your Message</div>
    <span class="btn btn-solid send">Send Now</span>
  </div>
</section>

<footer class="footer" style="position:absolute;left:0;width:1200px">Copyright © 2017 Quelp Technologies. All Rights Reserved.</footer>

</body>
</html>
```